New business needs it's first website designed and coded for Wordpress

This is a new website for a new business. The business is called The Remote Tech Expert (TRTE). The business is based across multiple countries with the goal of providing workers in the Philippines opportunities to find work in international companies based in Australia, Singapore and New Zealand. The target market for TRTE is large enterprises (initially in Australia) looking for well legally structured business that knows how to recruit the top IT professionals and ensure that they are happy, all compliance, taxes and legals and professionally done and all services contracts are local to ensure enforceability.

We are looking for 10 pages (6 templates) for the website as follows:
Home
About Us
Services
Work from home full-timers
Work from office full-times
Work from home contractors
Work from office contractors
Careers Job Search
Employers Contact Us
Candidates Register your interest

Target Market(s)

IT Professionals in the Philippines & large enterprises in Australia, Singapore and New Zealand

Industry/Entity Type

IT Recruitment

Coding

Coded - Design and coding required

Number of Pages Required

5+ page

Requirements
Must have
• Please based style off logo file attached.

```html
<!DOCTYPE html>
<html lang="en">
<head>
<meta charset="utf-8">
<title>The Remote Tech Expert (TRTE)</title>
<link rel="stylesheet" href="https://fonts.googleapis.com/css2?family=Archivo+Black&family=Jost:wght@400;500;600;700&display=swap">
<style>
:root{
  --cyan:#00a6ea;
  --blue:#0b5fe8;
  --ink:#111111;
  --black:#000000;
  --white:#ffffff;
  --pale:#f2fbfd;
  --muted:#3a3a3a;
  --line:#9aa3ab;
}
*{box-sizing:border-box;margin:0;padding:0}
html,body{width:1200px;height:3914px;overflow:hidden;background:var(--white)}
body{font-family:'Jost',sans-serif;color:var(--ink);position:relative}
.section{position:absolute;left:0;width:1200px}
.display{font-family:'Archivo Black',sans-serif;text-transform:uppercase;line-height:1.04;letter-spacing:.3px;white-space:nowrap}
.eyebrow{font-family:'Jost',sans-serif;font-weight:600;font-size:19px;text-decoration:underline;text-underline-offset:4px;color:#333;text-transform:uppercase}
.body-copy{font-size:13.5px;line-height:1.55;color:var(--muted)}
.btn{position:absolute;display:inline-flex;align-items:center;gap:6px;background:var(--blue);color:var(--white);font-weight:600;font-size:12.5px;text-transform:uppercase;padding:0 20px;height:34px;border-radius:2px;white-space:nowrap}
.btn svg{width:13px;height:13px}
.photo{position:absolute}

/* top bar */
.topbar{top:0;height:64px}
.brand{position:absolute;font-weight:700;font-size:22px;color:var(--ink);display:flex;align-items:center;gap:10px}
.brand-mark{width:18px;height:18px;background:var(--cyan)}
.contact-row{position:absolute;right:62px;top:22px;display:flex;align-items:center;gap:10px;font-size:12.5px}
.contact-row .sep{width:1px;height:18px;background:#888}
.contact-row svg{width:14px;height:14px}
.dot{width:13px;height:13px;border-radius:50%;background:var(--blue)}

/* nav */
.nav{top:64px;height:47px;background:var(--black)}
.nav ul{list-style:none;position:absolute;left:86px;top:0;height:47px;display:flex;align-items:center;gap:34px}
.nav li{color:var(--white);font-weight:600;font-size:12.5px;text-transform:uppercase}
.nav li.active{color:var(--cyan)}
.nav .btn{right:70px;top:6px;height:35px}

/* hero */
.hero{top:111px;height:483px}
.hero-panel{position:absolute;left:0;top:0;width:600px;height:483px;background:var(--cyan)}
.hero h1{position:absolute;left:43px;top:86px;font-size:44px;color:var(--white)}
.hero p{position:absolute;left:43px;top:288px;font-size:27px;color:var(--white);line-height:1.05;width:540px}
.hero .btn{left:43px;top:361px}

/* about */
.about{top:594px;height:671px}
.about .eyebrow{position:absolute;left:625px;top:162px}
.about h2{position:absolute;left:625px;top:200px;font-size:28px}
.about .body-copy{position:absolute;left:625px;top:317px;width:515px;text-align:justify}
.about .btn{left:625px;top:469px}

/* partner */
.partner{top:1263px;height:262px;background:var(--black)}
.partner h2{position:absolute;left:60px;top:20px;width:710px;text-align:center;font-size:38px;color:var(--white)}
.partner .body-copy{position:absolute;left:84px;top:118px;width:665px;color:var(--white)}
.partner .btn{left:306px;top:209px}

/* services */
.services{top:1525px;height:816px;background:var(--pale)}
.services .eyebrow{position:absolute;left:50px;top:72px}
.services h2{position:absolute;left:50px;top:112px;font-size:29px}
.services .body-copy{position:absolute;left:50px;top:194px;width:735px}
.card{position:absolute;width:340px;height:182px;border:1.5px solid var(--line);border-radius:14px;background:transparent;text-align:center}
.card .icon{position:absolute;left:127px;top:-22px;width:86px;height:86px;border-radius:50%;background:var(--cyan)}
.card h3{position:absolute;left:0;right:0;top:83px;font-weight:500;font-size:19px}
.card .more{position:absolute;left:0;right:0;top:140px;font-size:12px;font-weight:600;color:var(--blue);display:flex;justify-content:center;align-items:center;gap:5px;text-transform:uppercase}
.card .more svg{width:12px;height:12px}

/* discover */
.discover{top:2341px;height:460px;background:var(--black)}
.discover h2{position:absolute;left:440px;top:112px;width:720px;text-align:center;font-size:38px;color:var(--white)}
.discover .body-copy{position:absolute;left:442px;top:222px;width:716px;color:var(--white);text-align:justify}
.discover .btn{left:701px;top:307px}

/* candidates */
.candidates{top:2801px;height:695px}
.candidates .eyebrow{position:absolute;left:50px;top:222px}
.candidates h2{position:absolute;left:50px;top:262px;font-size:31px}
.candidates .body-copy{position:absolute;left:50px;top:351px;width:540px;text-align:justify}
.candidates .btn{left:50px;top:434px}

/* footer */
.footer{top:3496px;height:418px;background:var(--black);color:var(--white)}
.footer .brand{color:var(--white);left:68px;top:96px;font-size:21px}
.footer .tagline{position:absolute;left:68px;top:158px;font-size:15px;line-height:1.1;width:250px}
.footer .socials{position:absolute;left:153px;top:205px;display:flex;gap:12px}
.footer .socials span{width:10px;height:10px;border-radius:50%;background:var(--blue)}
.footer h4{position:absolute;font-weight:600;font-size:16px;text-transform:uppercase}
.footer ul{position:absolute;list-style:none}
.footer li{display:flex;align-items:flex-start;gap:8px;font-size:13px;text-transform:uppercase;line-height:1.3;margin-bottom:6px}
.footer li svg{width:11px;height:11px;margin-top:3px;flex:none}
.footer .plain li{text-transform:none;font-size:14px}
.copyright{position:absolute;left:0;width:1200px;top:299px;text-align:center;font-size:15px}
</style>
</head>
<body>

<svg width="0" height="0" style="position:absolute">
  <defs>
    <symbol id="arrow-circle" viewBox="0 0 16 16"><circle cx="8" cy="8" r="6.8" fill="none" stroke="currentColor" stroke-width="1.5"/><path d="M4.8 8h6M8.4 5.4 11 8l-2.6 2.6" fill="none" stroke="currentColor" stroke-width="1.5" stroke-linecap="round" stroke-linejoin="round"/></symbol>
    <symbol id="arrow-solid" viewBox="0 0 16 16"><circle cx="8" cy="8" r="8" fill="#1da1f2"/><path d="M4.6 8h6.2M8.4 5.2 11.2 8l-2.8 2.8" fill="none" stroke="#000" stroke-width="1.7" stroke-linecap="round" stroke-linejoin="round"/></symbol>
    <symbol id="pin" viewBox="0 0 16 16"><path d="M8 1a5 5 0 0 0-5 5c0 3.8 5 9 5 9s5-5.2 5-9a5 5 0 0 0-5-5zm0 7a2 2 0 1 1 0-4 2 2 0 0 1 0 4z" fill="#1da1f2"/></symbol>
    <symbol id="mail" viewBox="0 0 16 16"><path d="M8 1 1 6v9h14V6zM3 7l5 3.5L13 7v6H3z" fill="#1da1f2"/></symbol>
    <symbol id="phone" viewBox="0 0 16 16"><path d="M4 1.5 6.5 5 5 6.6c.9 1.9 2.4 3.4 4.3 4.3L10.9 9.4 14.5 12 13 14.5C7 14 2 9 1.5 3z" fill="#1da1f2"/></symbol>
  </defs>
</svg>

<header class="section topbar">
  <div class="brand" style="left:55px;top:18px"><span class="brand-mark"></span>The Remote Tech Expert</div>
  <div class="contact-row">
    <svg><use href="#pin"/></svg><span>Connecting Top Filipino IT Talent with Global Opportunities</span>
    <span class="sep"></span>
    <svg><use href="#mail"/></svg><span>hello@remotetechexpert.example</span>
    <span class="sep"></span>
    <svg><use href="#phone"/></svg><span>1800 555 0199</span>
    <span class="sep"></span><span class="dot"></span>
    <span class="sep"></span><span class="dot"></span>
    <span class="sep"></span><span class="dot"></span>
  </div>
</header>

<nav class="section nav">
  <ul>
    <li class="active">Home</li>
    <li>About Us</li>
    <li>Services &nbsp;▾</li>
    <li>Careers Job Search</li>
    <li>Employers Contact Us</li>
    <li>Candidates – Register Your Interest</li>
  </ul>
  <span class="btn">Contact Us <svg><use href="#arrow-circle"/></svg></span>
</nav>

<section class="section hero">
  <div class="hero-panel"></div>
  <h1 class="display">Welcome to the<br>Remote Tech<br>Expert<br>(TRTE)</h1>
  <p>Connecting Top Filipino IT Talent with Global Opportunities!</p>
  <span class="btn">Get Started Now <svg><use href="#arrow-circle"/></svg></span>
  <div class="photo" role="img" aria-label="Three smiling IT professionals in business attire working at a laptop in an office" style="left:600px;top:0;width:600px;height:483px;background:linear-gradient(135deg,#8a8d92,#3e4250 55%,#20242e)"></div>
</section>

<section class="section about">
  <div class="photo" role="img" aria-label="Two young professionals standing together holding a tablet" style="left:76px;top:95px;width:248px;height:477px;border-radius:22px;background:linear-gradient(160deg,#d9d6d0,#b89a5a 60%,#2c3448)"></div>
  <div class="photo" role="img" aria-label="Two young professionals smiling, one holding a folder" style="left:328px;top:95px;width:248px;height:477px;border-radius:22px;background:linear-gradient(160deg,#e6e4df,#7d7f86 55%,#1d2029)"></div>
  <div class="eyebrow">About TRTE</div>
  <h2 class="display">Empowering Filipino IT<br>Talent, Elevating Global<br>Businesses</h2>
  <p class="body-copy">At TRTE, we are driven by a mission to connect top-tier IT professionals in the Philippines with global opportunities. With a focus on Australia, Singapore, and New Zealand, we offer businesses a seamless process to recruit, manage, and retain high-performing IT teams. Our commitment to compliance, legal integrity, and employee satisfaction ensures mutual success for employers and professionals alike.</p>
  <span class="btn">Know More About Us <svg><use href="#arrow-circle"/></svg></span>
</section>

<section class="section partner">
  <h2 class="display">Partner with TRTE for<br>Exceptional IT Talent</h2>
  <p class="body-copy">Looking for top IT professionals to join your team? Contact TRTE today to discuss your recruitment needs. Our experts will guide you through every step, ensuring you find the perfect match for your business.</p>
  <span class="btn">Employers - Contact Us <svg><use href="#arrow-circle"/></svg></span>
</section>
<div class="photo" role="img" aria-label="Three cheering professionals in business wear celebrating" style="left:820px;top:1155px;width:305px;height:355px;background:linear-gradient(180deg,#d9c8cf,#5b5d68 55%,#1c1d22);border-radius:40% 40% 6px 6px"></div>

<section class="section services">
  <div class="eyebrow">Our Services</div>
  <h2 class="display">Comprehensive IT Recruitment and<br>Workforce Solutions</h2>
  <p class="body-copy">From full-time roles to contract positions, TRTE offers a suite of services designed to meet the diverse needs of large enterprises.</p>

  <div class="card" style="left:84px;top:301px"><div class="icon" role="img" aria-label="Icon of a person working at a desk at home"></div><h3>Work-From-Home Full-Timers</h3><div class="more">Know More <svg><use href="#arrow-circle"/></svg></div></div>
  <div class="card" style="left:454px;top:301px"><div class="icon" role="img" aria-label="Icon of a person working at an office desk"></div><h3>Office-Based Full-Timers</h3><div class="more">Know More <svg><use href="#arrow-circle"/></svg></div></div>
  <div class="card" style="left:84px;top:523px"><div class="icon" role="img" aria-label="Icon of a remote contractor at a workstation"></div><h3>Remote Contractors</h3><div class="more">Know More <svg><use href="#arrow-circle"/></svg></div></div>
  <div class="card" style="left:454px;top:523px"><div class="icon" role="img" aria-label="Icon of a team meeting around a table"></div><h3>On-Site Contractors</h3><div class="more">Know More <svg><use href="#arrow-circle"/></svg></div></div>

  <div class="photo" role="img" aria-label="Three thoughtful professionals standing in business attire" style="left:805px;top:117px;width:320px;height:615px;background:linear-gradient(180deg,#c9b9c4,#3b3e4d 50%,#14151a);border-radius:45% 45% 8px 8px"></div>
</section>

<section class="section discover">
  <h2 class="display">Discover Your Next IT<br>Opportunity with TRTE</h2>
  <p class="body-copy">Are you an IT professional in the Philippines looking to work with global companies? Explore our job board for exciting opportunities in Australia, Singapore, and New Zealand. Join TRTE and take the next step in your career.</p>
  <span class="btn">Careers - Job Search <svg><use href="#arrow-circle"/></svg></span>
</section>
<div class="photo" role="img" aria-label="Smiling young professional in a navy suit" style="left:45px;top:2234px;width:290px;height:563px;background:linear-gradient(180deg,#c9a68c 0,#1f3a7a 35%,#0e1f4a);border-radius:45% 45% 4px 4px"></div>

<section class="section candidates">
  <div class="eyebrow">Candidates - Register Your Interest</div>
  <h2 class="display">Join TRTE and Unlock<br>Global IT Opportunities</h2>
  <p class="body-copy">Ready to take your IT career to the next level? Register your interest with TRTE and gain access to international opportunities with leading companies in Australia, Singapore, and New Zealand. Let us connect you with the right role.</p>
  <span class="btn">Registration Now <svg><use href="#arrow-circle"/></svg></span>
  <div class="photo" role="img" aria-label="Four confident professionals standing with arms crossed" style="left:684px;top:95px;width:418px;height:510px;background:linear-gradient(180deg,#d8c6b8,#2a2c33 40%,#18191d);border-radius:40% 40% 8px 8px"></div>
</section>

<footer class="section footer">
  <div class="brand"><span class="brand-mark"></span>TRTE</div>
  <p class="tagline">Connecting Top Filipino IT Talent With Global Opportunities!</p>
  <div class="socials"><span></span><span></span><span></span></div>

  <h4 style="left:401px;top:96px">Our Company</h4>
  <ul style="left:347px;top:130px;width:230px">
    <li><svg><use href="#arrow-solid"/></svg>Home</li>
    <li><svg><use href="#arrow-solid"/></svg>About Us</li>
    <li><svg><use href="#arrow-solid"/></svg>Careers Job Search</li>
    <li><svg><use href="#arrow-solid"/></svg>Employers Contact Us</li>
    <li><svg><use href="#arrow-solid"/></svg>Candidates – Register Your Interest</li>
  </ul>

  <h4 style="left:683px;top:96px">Our Services</h4>
  <ul style="left:625px;top:130px;width:260px">
    <li><svg><use href="#arrow-solid"/></svg>Work-From-Home Full-Timers</li>
    <li><svg><use href="#arrow-solid"/></svg>Office-Based Full-Timers</li>
    <li><svg><use href="#arrow-solid"/></svg>Remote Contractors</li>
    <li><svg><use href="#arrow-solid"/></svg>On-Site Contractors</li>
  </ul>

  <h4 style="left:962px;top:96px">Get In Touch</h4>
  <ul class="plain" style="left:903px;top:130px;width:290px">
    <li><svg><use href="#pin"/></svg>Your Address Will Be Here</li>
    <li><svg><use href="#mail"/></svg>hello@remotetechexpert.example</li>
    <li><svg><use href="#phone"/></svg>1800 555 0199</li>
  </ul>

  <p class="copyright">Copyright © 2025 TRTE. All Rights Reserved.</p>
</footer>

</body>
</html>
```